Classic Minimalistic Business Card

Design a classic, minimalistic Business Card. Please find inspiration in the attached Classic Minimalistic examples. My information:
Name: Glen Ovamir
Company: Ovamir Capital
Logo: OC
Address: 1470 N Thornwick Rd, Suite 210 | Brenmoor, IL 60899
Phone: 630-555-0192
Email: glenovamir@pvt.insure
Slogan: Building Strength Through Capital

Feel free to leave out any of the information above except my name.

I have selected Double-sided, but I am also open to Single-sided

Target Market(s)

22-70. income greater than 150k/year

Industry/Entity Type

Finance

Contact Information for Business Card

See Project Description

Requirements
Must have
• Ivory or "antiqued" background similar to the reference pictures

```html
<!DOCTYPE html>
<html lang="en">
<head>
<meta charset="utf-8">
<title>Ovamir Capital — Business Card</title>
<link rel="stylesheet" href="https://fonts.googleapis.com/css2?family=Courier+Prime:wght@400;700&display=swap">
<style>
  :root {
    --backdrop: #262626;
    --ivory: #f1ecc6;
    --ivory-shade: rgba(120, 115, 90, 0.16);
    --ink: #0c0c0c;
    --type: "Courier Prime", "Courier New", monospace;
  }
  * { margin: 0; padding: 0; box-sizing: border-box; }
  html, body {
    width: 1200px; height: 1200px; overflow: hidden;
    background: var(--backdrop);
  }
  .canvas { position: relative; width: 1200px; height: 1200px; }

  .card {
    position: absolute;
    width: 700px; height: 399px;
    border-radius: 26px;
    background:
      radial-gradient(circle at 12% 85%, var(--ivory-shade), transparent 28%),
      radial-gradient(circle at 80% 12%, var(--ivory-shade), transparent 30%),
      radial-gradient(circle at 35% 10%, rgba(120,115,90,0.10), transparent 22%),
      radial-gradient(circle at 95% 70%, rgba(120,115,90,0.10), transparent 25%),
      var(--ivory);
    box-shadow: 0 6px 16px rgba(0,0,0,0.35);
    color: var(--ink);
    font-family: var(--type);
  }
  .card--front { left: 219px; top: 185px; }
  .card--back  { left: 227px; top: 617px; }

  .brand-square { position: absolute; background: var(--ink); }
  .card--front .brand-square { left: 82px; top: 130px; width: 167px; height: 167px; }
  .card--back  .brand-square { left: 492px; top: 51px; width: 165px; height: 165px; }

  .wordmark__primary {
    position: absolute; left: 258px; top: 150px;
    font-size: 80px; font-weight: 700; line-height: 1;
    letter-spacing: 2px; white-space: nowrap;
  }
  .wordmark__secondary {
    position: absolute; left: 266px; top: 221px;
    font-size: 28px; font-weight: 400; line-height: 1;
    letter-spacing: 32px; white-space: nowrap;
  }
  .tagline {
    position: absolute; left: 261px; top: 251px;
    font-size: 17px; font-weight: 700; letter-spacing: 0.5px;
    text-transform: uppercase; white-space: nowrap; line-height: 1;
  }

  .holder-name {
    position: absolute; left: 28px; top: 110px;
    font-size: 42px; font-weight: 400; white-space: nowrap; line-height: 1.1;
  }
  .contact {
    position: absolute; left: 28px; top: 168px;
    font-size: 24px; line-height: 31px; white-space: nowrap;
  }
  .address {
    position: absolute; left: 28px; top: 288px;
    font-size: 21px; line-height: 27px; white-space: nowrap;
  }
</style>
</head>
<body>
<main class="canvas">
  <section class="card card--front" aria-label="Card front">
    <div class="brand-square" aria-hidden="true"></div>
    <h1 class="wordmark">
      <span class="wordmark__primary">OVAMIR</span>
      <span class="wordmark__secondary">CAPITAL</span>
    </h1>
    <p class="tagline">Building Strength Through Capital</p>
  </section>

  <section class="card card--back" aria-label="Card back">
    <h2 class="holder-name">Glen Ovamir</h2>
    <p class="contact">glenovamir@pvt.insure<br>630-555-0192</p>
    <p class="address">1470 N Thornwick Rd,<br>Suite 210 | Brenmoor, IL 60899</p>
    <div class="brand-square" aria-hidden="true"></div>
  </section>
</main>
</body>
</html>
```